Website Design for Brackwood Academy

Brackwood Academy is a new start up professional college established to meet the educational needs of young adults, working adults, organisations and employers. We offer a variety of programs ranging from ICT, Healthcare, Business, Aviation, Professional courses. We will also be providing online courses in the very near future
We would like a modern, fresh conservative, sophisticated and professional appealing website for students. We want to keep our logo the same with the logo colours blended in as the primary colours and focus.
Unless you have a good reason for not, we would like the page to be the whole with of the screen like many websites are for the moment. The colour scheme should have a white or very light background.
We need a sliding header with pictures of young adults and professional people in college, pictures of Harare City, Students in a computer lab, adults students in Healthcare uniforms, etc…. Please see http://www.tamberfordcampus.example/
Main menu items: Home, About Us, Programs (When you hover the mouse on Programs, we should see the different Schools in the Academy. Business School, Healthcare School, ICT School, Hair & Beauty School, Aviation School, Executive School), Admissions (downloadable application form in PDF), International Students, News & Events, Contact Us
We need 10 pages designed as a start. These need to be scalable as we will be adding more pages when we start adding the content: The home page can be considerably different from the other pages. It needs to grab the attention of students and parents and direct them where they need to go e.g. the Academy schools. These should be visible on the home page as in the http://www.tamberfordcampus.example/ when clicked the School should open in a different page. That page will also have sub-pages for the individual courses within the School
The home page should include a scrolling widget where we can put our affiliated organisations. This should be at the bottom but before the Site map
An element of lead generation (either form fields or link to contact form should be included (for instance, “apply now” or “request more information” type buttons ).
Inspirational website & template:
http://www.tamberfordcampus.example/
http://www.zentrovault.example/RX-Scholar-Bootstrap-template-481927635.html
Our website objective is to
Provides information to prospective students about the Academy programs, we offer etc
1. Impress our participants with our fresh vibrant website design
2. User friendly with necessary info all seen on home page without scrolling down yet.
3. create awareness
4.will be integrating with facebook and twitter
The website should be:
- Easy to navigate
- SEO friendly design
Target Market(s)
Our Target market is the ages of 18-40yrs Professionals and non professionals
On High Income
Industry/Entity Type
Education
Number of Pages Required
5+ page
Requirements
Must have
- Must be responsive
- Data which I will provide later
Nice to have
- Would be great if you can get the same template as this one http://www.tamberfordcampus.example/ or a much better one
Should not have
- No too much page scrolling
- Not too squashed
- Avoid Too many colours

```html
<!DOCTYPE html>
<html lang="en">
<head>
<meta charset="utf-8">
<title>Brackwood Academy</title>
<link href="https://fonts.googleapis.com/css2?family=Raleway:wght@500;600;700&family=Open+Sans:wght@400;600;700&display=swap" rel="stylesheet">
<style>
:root{
  --navy:#0d3466;
  --navy-dark:#0a2850;
  --orange:#f5a300;
  --gold:#f7b928;
  --ink:#2b2b2b;
  --text:#6b6b6b;
  --rule:#e4e4e4;
  --footer:#f1f1f1;
  --footer-bar:#e6e6e6;
  --white:#ffffff;
}
*{margin:0;padding:0;box-sizing:border-box}
html,body{width:686px;height:1200px;overflow:hidden;background:var(--white)}
body{font-family:"Open Sans",Arial,sans-serif;color:var(--text);position:relative}

/* Header */
.site-header{height:45px;display:flex;align-items:center;justify-content:space-between;padding:0 22px 0 30px}
.brand{display:flex;align-items:center;gap:5px;background:var(--navy);padding:5px 9px 5px 6px;height:30px}
.brand-mark{width:14px;height:14px;background:var(--orange)}
.brand-name{font-family:"Raleway",sans-serif;font-weight:700;font-size:12.5px;color:var(--orange);letter-spacing:.2px}
.main-nav{display:flex;gap:13px}
.main-nav a{font-size:6.8px;font-weight:700;color:var(--ink);text-decoration:none;letter-spacing:.3px}
.main-nav a.active{color:var(--navy)}

/* Hero slider */
.hero{position:relative;height:320px}
.hero-photo{position:absolute;inset:0;background:linear-gradient(100deg,#7d9a4f 0%,#a9bd7a 22%,#c9b79a 45%,#e4cdb6 65%,#c58e73 85%,#9a5e4a 100%)}
.slider-arrow{position:absolute;top:150px}
.slider-arrow.prev{left:10px}
.slider-arrow.next{right:10px}
.hero-title{position:absolute;left:0;right:0;top:228px;text-align:center;font-family:"Raleway",sans-serif;font-size:30px;font-weight:500;letter-spacing:6px;color:rgba(255,255,255,.55)}

/* Sections */
.section-title{font-family:"Raleway",sans-serif;font-weight:600;color:var(--navy-dark);text-align:center;letter-spacing:.5px}
.welcome{padding-top:40px}
.welcome .section-title{font-size:16px}
.title-rule{width:300px;height:1px;background:var(--rule);margin:8px auto 0}
.welcome p{width:500px;margin:7px auto 0;font-size:6.4px;line-height:9.5px;text-align:center}

.services{padding-top:36px}
.services .section-title{font-size:16px}
.service-grid{width:494px;margin:20px auto 0;display:grid;grid-template-columns:repeat(3,154px);column-gap:16px;row-gap:24px}
.service-card{height:125px;background:var(--navy);padding:12px 11px}
.service-card.featured{background:var(--orange)}
.service-head{display:flex;align-items:center;gap:6px}
.service-head h3{font-family:"Raleway",sans-serif;font-size:10px;font-weight:600;color:var(--gold)}
.service-card.featured h3{color:var(--navy-dark)}
.service-card p{margin-top:9px;font-size:6.3px;line-height:9px;color:#d9e1ec}
.service-card.featured p{color:#fff6df}

.testimonials{padding-top:48px}
.testimonials .section-title{font-size:20px;letter-spacing:1px}
.testimonials p{width:540px;margin:28px auto 0;font-size:6.4px;line-height:9.5px;text-align:center}
.dots{display:flex;justify-content:center;gap:5px;margin-top:36px}
.dots span{width:5px;height:5px;border-radius:50%;background:#c5c5c5}
.dots span.on{background:#555}

/* Footer */
.site-footer{position:absolute;left:0;right:0;top:1040px;height:160px;background:var(--footer)}
.footer-cols{display:grid;grid-template-columns:107px 172px 148px 150px;padding:16px 0 0 30px}
.footer-col h4{font-size:7px;font-weight:700;color:var(--ink);margin-bottom:9px}
.footer-col ul{list-style:none}
.footer-col li{font-size:6px;color:var(--text);line-height:11px}
.feed-item{display:flex;gap:5px;margin-bottom:9px}
.feed-dot{width:9px;height:9px;border-radius:50%;background:#9aa7b8;flex:none}
.feed-item strong{display:block;font-size:6px;color:var(--ink);font-weight:600}
.feed-item span{display:block;font-size:5.6px;line-height:8px}
.footer-bar{position:absolute;left:0;right:0;bottom:0;height:20px;background:var(--footer-bar);display:flex;justify-content:space-between;align-items:center;padding:0 22px;font-size:5.6px}
</style>
</head>
<body>

<header class="site-header">
  <div class="brand">
    <span class="brand-mark"></span>
    <span class="brand-name">Brackwood Academy</span>
  </div>
  <nav class="main-nav">
    <a href="#" class="active">HOME</a>
    <a href="#">ABOUT US</a>
    <a href="#">PROGRAMS</a>
    <a href="#">ADMISSIONS</a>
    <a href="#">INTERNATIONAL STUDENTS</a>
    <a href="#">NEWS &amp; EVENTS</a>
    <a href="#">CONTACT US</a>
  </nav>
</header>

<section class="hero">
  <div class="hero-photo" role="img" aria-label="Group of smiling young adult students outdoors on campus"></div>
  <svg class="slider-arrow prev" width="16" height="16" viewBox="0 0 16 16"><circle cx="8" cy="8" r="8" fill="rgba(0,0,0,.35)"/><path d="M9.5 4.5 6 8l3.5 3.5" stroke="#fff" stroke-width="1.5" fill="none"/></svg>
  <svg class="slider-arrow next" width="16" height="16" viewBox="0 0 16 16"><circle cx="8" cy="8" r="8" fill="rgba(0,0,0,.35)"/><path d="M6.5 4.5 10 8l-3.5 3.5" stroke="#fff" stroke-width="1.5" fill="none"/></svg>
  <div class="hero-title">BRACKWOOD ACADEMY</div>
</section>

<section class="welcome">
  <h2 class="section-title">WELCOME TO BRACKWOOD ACADEMY</h2>
  <div class="title-rule"></div>
  <p>Brackwood Academy offers practical, career-focused programmes for young adults and working professionals. Our lecturers bring real industry experience into every class, and our flexible timetables make it possible to study while you work. Explore our schools below, meet our student advisers and find the course that moves your career forward this year.</p>
</section>

<section class="services">
  <h2 class="section-title">OUR SERVICES</h2>
  <div class="service-grid">
    <article class="service-card featured">
      <div class="service-head">
        <svg width="14" height="13" viewBox="0 0 14 13"><rect x="1" y="3" width="12" height="9" rx="1" fill="#0a2850"/><rect x="5" y="1" width="4" height="3" fill="none" stroke="#0a2850" stroke-width="1.2"/></svg>
        <h3>Business School</h3>
      </div>
      <p>Accounting, marketing and management courses built around real case studies, helping you plan, lead and grow organisations with confidence.</p>
    </article>
    <article class="service-card">
      <div class="service-head">
        <svg width="13" height="13" viewBox="0 0 13 13"><path d="M4.5 0h4v4.5H13v4H8.5V13h-4V8.5H0v-4h4.5z" fill="#f7b928"/></svg>
        <h3>Healthcare School</h3>
      </div>
      <p>Nursing assistance, patient care and health administration taught in modern practical rooms by qualified staff with hospital experience.</p>
    </article>
    <article class="service-card">
      <div class="service-head">
        <svg width="14" height="13" viewBox="0 0 14 13"><rect x="1" y="1" width="12" height="8" fill="none" stroke="#f7b928" stroke-width="1.4"/><rect x="5" y="10" width="4" height="2" fill="#f7b928"/></svg>
        <h3>ICT School</h3>
      </div>
      <p>Networking, programming and systems support delivered in fully equipped computer labs with industry certification preparation included.</p>
    </article>
    <article class="service-card">
      <div class="service-head">
        <svg width="13" height="13" viewBox="0 0 13 13"><circle cx="3" cy="10" r="2" fill="none" stroke="#f7b928" stroke-width="1.3"/><circle cx="10" cy="10" r="2" fill="none" stroke="#f7b928" stroke-width="1.3"/><path d="M4.3 8.5 10 1M8.7 8.5 3 1" stroke="#f7b928" stroke-width="1.3"/></svg>
        <h3>Hair &amp; Beauty School</h3>
      </div>
      <p>Hairdressing, styling and beauty therapy programmes that combine salon practice with the business skills to open your own studio.</p>
    </article>
    <article class="service-card">
      <div class="service-head">
        <svg width="14" height="13" viewBox="0 0 14 13"><path d="M1 7.5 13 3l-1 2-4 2.5L7 12 6 12l.3-3.8L3 9.5 2 8z" fill="#f7b928"/></svg>
        <h3>Aviation School</h3>
      </div>
      <p>Cabin crew, ground handling and travel operations courses designed with airline partners to prepare you for a career in flight.</p>
    </article>
    <article class="service-card">
      <div class="service-head">
        <svg width="13" height="13" viewBox="0 0 13 13"><path d="M5 1h3l-.6 2 1.6 7-2.5 2.5L4 10l1.6-7z" fill="#f7b928"/></svg>
        <h3>Executive School</h3>
      </div>
      <p>Short leadership and strategy programmes for managers and employers, scheduled around busy working weeks and tailored to your team.</p>
    </article>
  </div>
</section>

<section class="testimonials">
  <h2 class="section-title">TESTIMONIALS</h2>
  <p>Studying at Brackwood Academy changed the way I see my future. The lecturers were patient and knowledgeable, the classes were practical, and the support team helped me balance my course with a full-time job. Within months of finishing my diploma I was promoted, and I am already planning my next course here.</p>
  <div class="dots"><span class="on"></span><span></span><span></span><span></span></div>
</section>

<footer class="site-footer">
  <div class="footer-cols">
    <div class="footer-col">
      <h4>Quick Links</h4>
      <ul><li>Home</li><li>About Us</li><li>Programs</li><li>Admissions</li><li>International Students</li><li>News &amp; Events</li><li>Contact Us</li></ul>
    </div>
    <div class="footer-col">
      <h4>Our Programs</h4>
      <ul><li>Business School</li><li>Healthcare School</li><li>ICT School</li><li>Hair &amp; Beauty School</li><li>Aviation School</li><li>Executive School</li></ul>
    </div>
    <div class="footer-col">
      <h4>Community Feed</h4>
      <div class="feed-item"><span class="feed-dot"></span><div><strong>Brackwood Academy</strong><span>Open day this Saturday, all welcome</span></div></div>
      <div class="feed-item"><span class="feed-dot"></span><div><strong>Brackwood Academy</strong><span>Enrolment for the new term is open</span></div></div>
    </div>
    <div class="footer-col">
      <h4>Campus Updates</h4>
      <div class="feed-item"><span class="feed-dot"></span><div><strong>Brackwood Academy</strong><span>New aviation intake starts in March</span></div></div>
      <div class="feed-item"><span class="feed-dot"></span><div><strong>Brackwood Academy</strong><span>Meet our healthcare lecturers</span></div></div>
    </div>
  </div>
  <div class="footer-bar">
    <span>© 2016 Brackwood Academy. All Rights Reserved</span>
    <span>Terms &amp; Conditions | Privacy Policy</span>
  </div>
</footer>

</body>
</html>
```